UX Design for Analytics Web Application

http://tovelunigroup.com/
We are tech & consulting company with analytics products (web applications), located at Rio de Janeiro, Brazil.

We are searching a partner do develop UX for our products, i.e, aesthetics, usability, HTML/CSS.

Currently we have a product suite and the goal is to make a pilot re-design project with one of our products.

The product of interest is interactive webapp that aims at data analysis, significantly different from blogs, e-commerce or landing pages.

We do have a software development team but we lack an UX & HTML expert. Currently we use Bootstrap templates but the results are insatisfatory.

So, the project scope is, to develop the arts (UX, aesthetics, etc) along with the code/mockup (HTML/CSS) for one of our product (3 pages).

This is a pilot project and there's potential to rehire for our other products. Code quality is of importance.

More details and specification can be found in attached files.

Target Market(s)

Executives, managers & consultants

Industry/Entity Type

It Company

Coding

Coded - Design and coding required

Number of Pages Required

3 page

Font styles to use
Sans Serif

Requirements
Must have
• (see attached files, prefer the pptx version))
• -Responsive
Nice to have
• (see attached files, prefer the pptx version)
Should not have
• -Avoid Green, Red and Yellow colors. They have a meaning of good, bad and average in our products.

```html
<!DOCTYPE html>
<html lang="en">
<head>
<meta charset="utf-8">
<title>Analytics Dashboard</title>
<link href="https://fonts.googleapis.com/css2?family=Rubik:wght@300;400;500&display=swap" rel="stylesheet">
<style>
:root{
  --sidebar:#1f2a44;
  --sidebar-deep:#18213a;
  --sidebar-text:#d6dcec;
  --sidebar-muted:#a3acc6;
  --page:#eef1f7;
  --card:#ffffff;
  --line:#e6e9f1;
  --ink:#545b6b;
  --ink-strong:#3a4152;
  --blue:#3f7be0;
  --blue-soft:#e8f0fc;
  --cyan:#2aa5d8;
  --violet:#8f6fd6;
  --violet-soft:#f0ebfa;
  --indigo:#3d4fa8;
  --indigo-soft:#e9ebf7;
  --panel:#7c6bd0;
  --panel-deep:#3f32a8;
  --track:#e7eaf2;
}
*{box-sizing:border-box;margin:0;padding:0}
html,body{width:1200px;height:689px;overflow:hidden}
body{font-family:"Rubik",sans-serif;background:var(--page);color:var(--ink);position:relative}

.sidebar{position:absolute;left:0;top:0;width:224px;height:689px;background:var(--sidebar);color:var(--sidebar-text);overflow:hidden}
.brand{position:absolute;left:17px;top:12px;font-size:12px;color:var(--sidebar-muted);letter-spacing:.2px}
.search{position:absolute;left:16px;top:70px;width:190px;height:31px;border-radius:16px;background:var(--sidebar-deep);color:#8a93ad;font-size:13px;padding:8px 20px}
.nav{position:absolute;left:0;top:120px;width:224px;list-style:none}
.nav li{height:38.6px;display:flex;align-items:center;padding:0 17px;font-size:13.5px}
.nav li.heading{font-size:13px;letter-spacing:.3px}
.nav .ico{width:15px;height:15px;margin-right:14px;fill:none;stroke:var(--sidebar-text);stroke-width:1.8;flex:none}
.nav .chev{margin-left:auto;width:8px;height:8px;stroke:var(--sidebar-muted);fill:none;stroke-width:1.5}
.version{background:var(--blue);color:#fff;font-size:10.5px;border-radius:9px;padding:2px 7px;margin-left:4px}

.topbar{position:absolute;left:224px;top:0;width:976px;height:53px;background:#fff;box-shadow:0 1px 3px rgba(0,0,0,.06)}
.topbar svg{position:absolute;fill:none;stroke:#555;stroke-width:1.8}
.tb-text{position:absolute;top:18px;font-size:13.5px;color:#444;line-height:16px}
.badge{position:absolute;top:8px;width:19px;height:19px;border-radius:50%;color:#fff;font-size:10.5px;display:flex;align-items:center;justify-content:center}
.avatar{position:absolute;left:836px;top:12px;width:28px;height:28px;border-radius:50%;background:linear-gradient(135deg,#c3c7d3,#6b7080)}

.card{position:absolute;background:var(--card);box-shadow:0 1px 2px rgba(0,0,0,.05)}
.stats{left:248px;top:76px;width:927px;height:205px;display:flex}
.stat{flex:1;position:relative;text-align:center;border-right:1px solid var(--line)}
.stat:last-child{border-right:0}
.stat-value{margin-top:14px;font-size:28px;color:var(--ink)}
.stat-label{margin-top:6px;font-size:12.5px}
.spark{display:block;margin:12px auto 0}
.sub{display:flex;margin-top:14px}
.sub div{flex:1}
.sub > div:first-child{border-right:1px solid var(--line)}
.sub-value{font-size:21px}
.sub-label{margin-top:9px;font-size:12.5px;color:var(--ink)}
.tone-blue{color:var(--blue)}.tone-violet{color:var(--violet)}.tone-indigo{color:var(--indigo)}
.trend{width:9px;height:7px;margin-right:5px;fill:none;stroke-width:1.6;stroke:currentColor;vertical-align:1px}

.chart-card{left:248px;top:308px;width:608px;height:400px}
.legend{position:absolute;top:22px;width:100%;text-align:center;font-size:13.5px;color:var(--ink-strong)}
.legend span{display:inline-flex;align-items:center;margin:0 4px}
.legend i{width:11px;height:11px;border-radius:50%;margin-right:5px;display:inline-block}
.line-chart{position:absolute;left:0;top:0}
.totals{position:absolute;left:0;top:277px;width:608px;border-top:1px solid var(--line);display:flex;padding:0 12px}
.total{flex:1;text-align:center;padding-top:15px}
.total-label{font-size:13.5px}
.total-value{font-size:22px;color:var(--ink-strong);margin-top:2px}
.progress{width:121px;height:4px;background:var(--track);margin:13px auto 0;border-radius:2px}
.progress b{display:block;height:4px;width:70%;background:var(--blue);border-radius:2px}

.sales{left:885px;top:308px;width:290px;height:400px;background:var(--panel);color:#fff}
.sales-title{position:absolute;top:22px;width:100%;text-align:center;font-size:13.5px}
.bar-chart{position:absolute;left:0;top:0}
.sales-foot{position:absolute;top:306px;left:0;width:100%;border-top:1px solid rgba(255,255,255,.35)}
.btn{position:absolute;left:35px;top:336px;width:104px;height:30px;background:var(--panel-deep);color:#fff;font-size:13px;display:flex;align-items:center;justify-content:center;gap:6px}
.btn-note{position:absolute;left:152px;top:343px;font-size:13.5px}
</style>
</head>
<body>
<aside class="sidebar">
  <div class="brand">tovelunigroup.com</div>
  <div class="search">Search</div>
  <ul class="nav">
    <li><svg class="ico" viewBox="0 0 16 16"><path d="M2 8 8 2l6 6M4 7v7h8V7" fill="var(--sidebar-text)"/></svg>Dashboard<svg class="chev" viewBox="0 0 8 8"><path d="M2 1l3 3-3 3"/></svg></li>
    <li><svg class="ico" viewBox="0 0 16 16"><rect x="2" y="2" width="12" height="12"/><path d="M5 6h6M5 9h6"/></svg>Templates<svg class="chev" viewBox="0 0 8 8"><path d="M2 1l3 3-3 3"/></svg></li>
    <li class="heading">LAYOUTS</li>
    <li><svg class="ico" viewBox="0 0 16 16"><rect x="2" y="4" width="10" height="10"/><path d="M5 2h9v9"/></svg>Page layouts<svg class="chev" viewBox="0 0 8 8"><path d="M2 1l3 3-3 3"/></svg></li>
    <li><svg class="ico" viewBox="0 0 16 16"><path d="M2 4h12M2 8h12M2 12h12"/></svg>Navbars<svg class="chev" viewBox="0 0 8 8"><path d="M2 1l3 3-3 3"/></svg></li>
    <li><svg class="ico" viewBox="0 0 16 16"><rect x="5" y="2" width="6" height="12"/></svg>Vertical Nav<svg class="chev" viewBox="0 0 8 8"><path d="M2 1l3 3-3 3"/></svg></li>
    <li><svg class="ico" viewBox="0 0 16 16"><rect x="2" y="5" width="12" height="6"/></svg>Horizontal Nav<svg class="chev" viewBox="0 0 8 8"><path d="M2 1l3 3-3 3"/></svg></li>
    <li><svg class="ico" viewBox="0 0 16 16"><rect x="2" y="4" width="12" height="8"/></svg>Page Headers<svg class="chev" viewBox="0 0 8 8"><path d="M2 1l3 3-3 3"/></svg></li>
    <li><svg class="ico" viewBox="0 0 16 16"><path d="M8 2v8M5 7l3 3 3-3M3 14h10"/></svg>Footers<svg class="chev" viewBox="0 0 8 8"><path d="M2 1l3 3-3 3"/></svg></li>
    <li class="heading">GENERAL</li>
    <li><svg class="ico" viewBox="0 0 16 16"><path d="M3 12 11 4l2 2-8 8H3z"/></svg>Color Palette<svg class="chev" viewBox="0 0 8 8"><path d="M2 1l3 3-3 3"/></svg></li>
    <li><svg class="ico" viewBox="0 0 16 16"><circle cx="8" cy="6" r="4"/><path d="M6 12h4M7 14h2"/></svg>Starter kit<svg class="chev" viewBox="0 0 8 8"><path d="M2 1l3 3-3 3"/></svg></li>
    <li><svg class="ico" viewBox="0 0 16 16"><rect x="2" y="5" width="8" height="9"/><path d="M6 2h8v8"/></svg>Changelog<span class="version">1.2.2</span></li>
    <li><svg class="ico" viewBox="0 0 16 16"><path d="M1 8s3-5 7-5 7 5 7 5-3 5-7 5-7-5-7-5z"/><circle cx="8" cy="8" r="2"/></svg>Disabled Menu</li>
    <li><svg class="ico" viewBox="0 0 16 16"><path d="M2 4h12M2 8h12"/></svg>Menu levels</li>
  </ul>
</aside>

<header class="topbar">
  <svg style="left:28px;top:17px" width="19" height="16" viewBox="0 0 19 16"><path d="M1 2h17M1 8h17M1 14h17"/></svg>
  <svg style="left:79px;top:17px" width="17" height="17" viewBox="0 0 17 17"><circle cx="7" cy="7" r="5.5"/><path d="M11 11l5 5"/></svg>
  <svg style="left:127px;top:17px" width="17" height="17" viewBox="0 0 17 17"><path d="M1 6V1h5M11 1h5v5M16 11v5h-5M6 16H1v-5"/></svg>
  <span class="tb-text" style="left:171px">Mega</span>
  <svg style="left:212px;top:23px" width="8" height="6" viewBox="0 0 8 6"><path d="M1 1l3 3 3-3"/></svg>
  <svg style="left:632px;top:18px" width="16" height="16" viewBox="0 0 16 16"><circle cx="8" cy="8" r="6.5"/><path d="M1.5 8h13M8 1.5c-3 3.5-3 9.5 0 13M8 1.5c3 3.5 3 9.5 0 13"/></svg>
  <span class="tb-text" style="left:654px">English</span>
  <svg style="left:706px;top:23px" width="8" height="6" viewBox="0 0 8 6"><path d="M1 1l3 3 3-3"/></svg>
  <svg style="left:743px;top:18px" width="17" height="18" viewBox="0 0 17 18"><path d="M3 13V8a5.5 5.5 0 0 1 11 0v5l1.5 1.5h-14zM7 16.5h3"/></svg>
  <span class="badge" style="left:753px;background:var(--indigo)">5</span>
  <svg style="left:796px;top:20px" width="17" height="13" viewBox="0 0 17 13"><rect x="1" y="1" width="15" height="11"/><path d="M1 1l7.5 6L16 1"/></svg>
  <span class="badge" style="left:805px;background:var(--cyan)">8</span>
  <div class="avatar" role="img" aria-label="User profile photo"></div>
  <span class="tb-text" style="left:874px">Lena Marsh</span>
  <svg style="left:952px;top:23px" width="8" height="6" viewBox="0 0 8 6"><path d="M1 1l3 3 3-3"/></svg>
</header>

<section class="card stats">
  <div class="stat">
    <div class="stat-value">$84,962</div>
    <div class="stat-label">Monthly Profit</div>
    <svg class="spark" width="216" height="30" viewBox="0 0 216 30"><path d="M0 12C12 6 24 8 36 12S60 18 72 14 96 12 108 16 132 20 144 14 168 10 180 16 204 10 216 10V30H0z" fill="var(--blue-soft)"/><path d="M0 12C12 6 24 8 36 12S60 18 72 14 96 12 108 16 132 20 144 14 168 10 180 16 204 10 216 10" fill="none" stroke="var(--blue)" stroke-width="2"/></svg>
    <div class="sub">
      <div><div class="sub-value tone-blue">$8,200</div><div class="sub-label"><svg class="trend tone-blue" viewBox="0 0 9 7"><path d="M1 6l3.5-4L8 6"/></svg>Today</div></div>
      <div><div class="sub-value tone-blue">$5,400</div><div class="sub-label"><svg class="trend tone-blue" viewBox="0 0 9 7"><path d="M1 1l3.5 4L8 1"/></svg>Yesterday</div></div>
    </div>
  </div>
  <div class="stat">
    <div class="stat-value">1,879</div>
    <div class="stat-label">Total Employee</div>
    <svg class="spark" width="216" height="30" viewBox="0 0 216 30"><path d="M0 12C12 8 24 16 36 16S60 10 72 14 96 18 108 14 132 12 144 16 168 8 180 12 204 2 216 10V30H0z" fill="var(--violet-soft)"/><path d="M0 12C12 8 24 16 36 16S60 10 72 14 96 18 108 14 132 12 144 16 168 8 180 12 204 2 216 10" fill="none" stroke="var(--violet)" stroke-width="2"/></svg>
    <div class="sub">
      <div><div class="sub-value tone-violet">4789</div><div class="sub-label"><svg class="trend tone-violet" viewBox="0 0 9 7"><path d="M1 6l3.5-4L8 6"/></svg>This Quarter</div></div>
      <div><div class="sub-value tone-violet">389</div><div class="sub-label"><svg class="trend tone-violet" viewBox="0 0 9 7"><path d="M1 1l3.5 4L8 1"/></svg>Last Quarter</div></div>
    </div>
  </div>
  <div class="stat">
    <div class="stat-value">894</div>
    <div class="stat-label">Support Tickets</div>
    <svg class="spark" width="216" height="30" viewBox="0 0 216 30"><path d="M0 10C12 8 24 14 36 12S60 8 72 14 96 16 108 10 132 12 144 8 168 14 180 10 204 4 216 10V30H0z" fill="var(--indigo-soft)"/><path d="M0 10C12 8 24 14 36 12S60 8 72 14 96 16 108 10 132 12 144 8 168 14 180 10 204 4 216 10" fill="none" stroke="var(--indigo)" stroke-width="2"/></svg>
    <div class="sub">
      <div><div class="sub-value tone-indigo">81</div><div class="sub-label"><svg class="trend tone-indigo" viewBox="0 0 9 7"><path d="M1 6l3.5-4L8 6"/></svg>Critical</div></div>
      <div><div class="sub-value tone-indigo">498</div><div class="sub-label"><svg class="trend tone-indigo" viewBox="0 0 9 7"><path d="M1 1l3.5 4L8 1"/></svg>Low</div></div>
    </div>
  </div>
</section>

<section class="card chart-card">
  <div class="legend"><span><i style="background:var(--violet)"></i>Remain</span><span><i style="background:var(--cyan)"></i>Completed</span></div>
  <svg class="line-chart" width="608" height="277" viewBox="0 0 608 277">
    <path d="M0 125C28 125 29 89 57 89S84 113 111 113 139 151 167 151 195 120 223 120 250 95 277 95 302 79 328 79 358 153 387 153 414 103 441 103 469 136 496 136 524 160 552 160 580 129 608 129" fill="none" stroke="var(--cyan)" stroke-width="2.5"/>
    <path d="M0 196C28 196 29 232 57 232S84 259 111 259 139 251 167 251 195 195 223 195 250 244 277 244 302 253 328 253 358 195 387 195 414 207 441 207 469 259 496 259 524 213 552 213 580 232 608 232" fill="none" stroke="var(--violet)" stroke-width="2.5"/>
    <g fill="#fff" stroke="var(--cyan)" stroke-width="1.5">
      <circle cx="57" cy="89" r="3.5"/><circle cx="111" cy="113" r="3.5"/><circle cx="167" cy="151" r="3.5"/><circle cx="223" cy="120" r="3.5"/><circle cx="277" cy="95" r="3.5"/><circle cx="328" cy="79" r="3.5"/><circle cx="387" cy="153" r="3.5"/><circle cx="441" cy="103" r="3.5"/><circle cx="496" cy="136" r="3.5"/><circle cx="552" cy="160" r="3.5"/>
    </g>
    <g fill="#fff" stroke="var(--violet)" stroke-width="1.5">
      <circle cx="57" cy="232" r="3.5"/><circle cx="111" cy="259" r="3.5"/><circle cx="167" cy="251" r="3.5"/><circle cx="223" cy="195" r="3.5"/><circle cx="277" cy="244" r="3.5"/><circle cx="328" cy="253" r="3.5"/><circle cx="387" cy="195" r="3.5"/><circle cx="441" cy="207" r="3.5"/><circle cx="496" cy="259" r="3.5"/><circle cx="552" cy="213" r="3.5"/>
    </g>
  </svg>
  <div class="totals">
    <div class="total"><div class="total-label">Total Projects</div><div class="total-value">18</div><div class="progress"><b></b></div></div>
    <div class="total"><div class="total-label">Total Task</div><div class="total-value">125</div><div class="progress"><b></b></div></div>
    <div class="total"><div class="total-label">Completed Task</div><div class="total-value">242</div><div class="progress"><b></b></div></div>
    <div class="total"><div class="total-label">Total Revenue</div><div class="total-value">$11,582</div><div class="progress"><b style="width:88%"></b></div></div>
  </div>
</section>

<section class="card sales">
  <div class="sales-title">Total monthly Sales.</div>
  <svg class="bar-chart" width="290" height="300" viewBox="0 0 290 300">
    <g stroke="rgba(255,255,255,.75)" stroke-width="1">
      <path d="M72 76H250M72 120H250M72 163H250M72 207H250M72 249H250"/>
    </g>
    <g fill="#fff" font-family="Rubik, sans-serif" font-size="11" text-anchor="end">
      <text x="63" y="80">3,000</text><text x="63" y="124">2,250</text><text x="63" y="167">1,500</text><text x="63" y="211">750</text><text x="63" y="253">0</text>
    </g>
    <g fill="#fff">
      <rect x="76" y="142" width="4" height="107"/><rect x="91" y="113" width="4" height="136"/><rect x="105" y="165" width="4" height="84"/><rect x="120" y="174" width="4" height="75"/><rect x="135" y="154" width="4" height="95"/><rect x="150" y="125" width="4" height="124"/><rect x="164" y="142" width="4" height="107"/><rect x="179" y="113" width="4" height="136"/><rect x="194" y="142" width="4" height="107"/><rect x="208" y="159" width="4" height="90"/><rect x="223" y="174" width="4" height="75"/><rect x="238" y="125" width="4" height="124"/>
    </g>
    <g fill="#fff" font-family="Rubik, sans-serif" font-size="11" text-anchor="middle">
      <text x="93" y="272">Feb</text><text x="166" y="272">Jul</text><text x="239" y="272">Dec</text>
    </g>
  </svg>
  <div class="sales-foot"></div>
  <div class="btn">Statistics<svg width="12" height="11" viewBox="0 0 12 11" fill="#fff"><rect x="0" y="6" width="2" height="5"/><rect x="3.3" y="3" width="2" height="8"/><rect x="6.6" y="5" width="2" height="6"/><rect x="10" y="0" width="2" height="11"/></svg></div>
  <div class="btn-note">for the last year.</div>
</section>
</body>
</html>
```